Classic Minimalistic Business Card

Design a classic, minimalistic Business Card. Please find inspiration in the attached Classic Minimalistic examples. My information:
Name: Glen Ovamir
Company: Ovamir Capital
Logo: OC
Address: 1470 N Thornwick Rd, Suite 210 | Larkfield, WN 00000
Phone: 555-555-0192
Email: glenovamir@pvt.insure
Slogan: Building Strength Through Capital

Feel free to leave out any of the information above except my name.

I have selected Double-sided, but I am also open to Single-sided

Target Market(s)

22-70. income greater than 150k/year

Industry/Entity Type

Finance

Contact Information for Business Card

See Project Description

Requirements
Must have
• Ivory or "antiqued" background similar to the reference pictures

```html
<!DOCTYPE html>
<html lang="en">
<head>
<meta charset="utf-8">
<title>Ovamir Capital – Business Card</title>
<link rel="stylesheet" href="https://fonts.googleapis.com/css2?family=Special+Elite&family=Courier+Prime:wght@400;700&display=swap">
<style>
  :root {
    --board: #b1a086;
    --card-edge: #eadcc2;
    --card-glow: #f4ece0;
    --ink: #59533f;
    --ink-soft: #665d4d;
    --shadow: rgba(60, 50, 35, 0.55);
  }
  * { margin: 0; padding: 0; box-sizing: border-box; }
  html, body { width: 1200px; height: 771px; overflow: hidden; }
  body {
    background: var(--board);
    font-family: "Special Elite", "Courier Prime", monospace;
    color: var(--ink);
    position: relative;
  }
  .board-title {
    position: absolute;
    top: 84px; left: 0; width: 1200px;
    text-align: center;
    font-size: 27px;
    font-weight: 400;
    color: var(--ink-soft);
    letter-spacing: 0.5px;
  }
  .card {
    position: absolute;
    top: 225px;
    width: 412px; height: 235px;
    background: radial-gradient(ellipse 52% 62% at 50% 50%, var(--card-glow) 0%, var(--card-edge) 100%);
    text-align: center;
  }
  .card::after {
    content: "";
    position: absolute;
    left: 6px; right: 6px; bottom: -8px; height: 12px;
    z-index: -1;
    background: radial-gradient(ellipse 50% 100% at 25% 0%, var(--shadow), transparent 70%),
                radial-gradient(ellipse 50% 100% at 75% 0%, var(--shadow), transparent 70%);
    filter: blur(3px);
  }
  .card-front { left: 151px; }
  .card-back { left: 637px; }
  .brand-mark {
    position: absolute;
    top: 82px; left: 50%;
    width: 38px; height: 38px;
    margin-left: -19px;
    border: 2px solid var(--ink);
    border-radius: 50%;
  }
  .company {
    position: absolute; top: 140px; left: 0; width: 100%;
    font-size: 18px;
    letter-spacing: 4px;
    color: var(--ink);
  }
  .name {
    position: absolute; top: 86px; left: 0; width: 100%;
    font-size: 15px;
    letter-spacing: 4px;
  }
  .phone {
    position: absolute; top: 106px; left: 0; width: 100%;
    font-size: 27px;
    letter-spacing: 1.5px;
  }
  .email {
    position: absolute; top: 182px; left: 0; width: 100%;
    font-family: "Courier Prime", monospace;
    font-weight: 700;
    font-size: 14.5px;
  }
  .address {
    position: absolute; top: 204px; left: 0; width: 100%;
    font-family: "Courier Prime", monospace;
    font-size: 11.5px;
    white-space: nowrap;
  }
  .board-note {
    position: absolute;
    top: 578px; left: 105px; width: 990px;
    text-align: center;
    font-size: 13px;
    line-height: 17.3px;
    color: var(--ink-soft);
  }
</style>
</head>
<body>
  <h1 class="board-title">Ovamir Capital</h1>

  <section class="card card-front">
    <span class="brand-mark"></span>
    <div class="company">Ovamir Capital</div>
  </section>

  <section class="card card-back">
    <div class="name">Glen Ovamir</div>
    <div class="phone">555-555-0192</div>
    <div class="email">glenovamir@pvt.insure</div>
    <div class="address">1470 N Thornwick Rd, Suite 210 | Larkfield, WN 00000</div>
  </section>

  <p class="board-note">Lorem ipsum dolor sit amet, consectetuer adipiscing elit, sed diam nonummy nibh euismod tincidunt ut laoreet dolore magna aliquam erat volutpat. Ut wisi enim ad minim veniam, quis nostrud exerci tation ullamcorper suscipit lobortis nisl ut aliquip ex ea commodo consequat. Duis autem vel eum iriure dolor in hendrerit in vulputate velit esse molestie consequat, vel illum dolore eu feugiat nulla facilisis at vero eros et accumsan et iusto odio dignissim qui blandit praesent luptatum zzril delenit augue duis dolore te feugait nulla facilisi.</p>
</body>
</html>
```